Design some Business Cards for Ski Trainer

1. A namecard with orange and white major color for a female Ski instructor
2. Prefer using more icons
3. Please use the same logo of http://www.frostpeakcoaching.example/ ( as seen in attached file, but you may need to reconstruct the logo again)
4. text detail for the content is attached
5. Please DO NOT use traditional fonts
6. We would like to use the font "Showcard Gothic " for the company name "Frost & Peak Coaching"

```html
<!DOCTYPE html>
<html lang="en">
<head>
<meta charset="utf-8">
<title>Frost &amp; Peak Coaching – Business Cards</title>
<link rel="stylesheet" href="https://fonts.googleapis.com/css2?family=Bowlby+One+SC&family=Roboto:wght@400;500;700&display=swap">
<style>
  :root {
    --backdrop: #8a97aa;
    --orange: #f5821f;
    --ink: #111111;
    --night: #0d0d0d;
    --snow: #f3f3f0;
    --ice: #d6e2ef;
    --white: #ffffff;
    --text-dark: #2a2a2a;
  }
  * { box-sizing: border-box; margin: 0; padding: 0; }
  html, body { width: 1200px; height: 933px; overflow: hidden; }
  body {
    background: var(--backdrop);
    font-family: "Roboto", Arial, sans-serif;
    display: flex;
    align-items: center;
    justify-content: center;
    gap: 56px;
  }
  .card {
    position: relative;
    width: 520px;
    height: 300px;
    overflow: hidden;
    box-shadow: 0 10px 24px rgba(0,0,0,0.25);
  }
  .card-bg { position: absolute; inset: 0; width: 100%; height: 100%; }
  .brand-title {
    position: absolute;
    font-family: "Bowlby One SC", Impact, sans-serif;
    color: var(--orange);
    white-space: nowrap;
  }

  /* Front */
  .card-front { background: var(--snow); }
  .card-front .brand-title { top: 26px; left: 28px; font-size: 27px; }
  .brand-mark {
    position: absolute;
    display: flex;
    align-items: center;
    gap: 10px;
    font-family: "Bowlby One SC", Impact, sans-serif;
  }
  .card-front .brand-mark { top: 92px; left: 50%; transform: translateX(-50%); color: var(--white); font-size: 34px; }
  .brand-mark .dot { width: 34px; height: 34px; border-radius: 50%; background: currentColor; }

  /* Back */
  .card-back { background: var(--ice); }
  .card-back .brand-title { top: 40px; left: 24px; font-size: 17px; }
  .card-back .brand-mark { top: 150px; left: 66px; color: var(--orange); font-size: 40px; }
  .card-back .brand-mark .dot { width: 40px; height: 40px; }
  .holder { position: absolute; top: 28px; right: 22px; text-align: left; }
  .holder-name { font-family: "Bowlby One SC", Impact, sans-serif; font-size: 19px; color: var(--ink); letter-spacing: 0.5px; }
  .holder-role { font-size: 9.5px; color: var(--text-dark); margin-top: 1px; }
  .contact-rail {
    position: absolute; top: 96px; left: 292px; width: 30px; bottom: 0;
    background: var(--orange);
    display: flex; flex-direction: column; align-items: center;
    padding-top: 14px; gap: 22px;
  }
  .contact-rail svg { width: 16px; height: 16px; }
  .contact-list {
    position: absolute; top: 108px; left: 334px;
    list-style: none; display: flex; flex-direction: column; gap: 21px;
    font-size: 11.5px; color: var(--text-dark);
  }
  .contact-list li { height: 16px; line-height: 16px; white-space: nowrap; }
</style>
</head>
<body>

  <section class="card card-front" aria-label="Business card front">
    <svg class="card-bg" viewBox="0 0 520 300" preserveAspectRatio="none" aria-hidden="true">
      <path d="M0 0 H520 V118 C440 96 380 138 290 166 C200 194 110 178 0 210 Z" fill="var(--night)"/>
      <path d="M0 248 C120 226 250 250 380 236 C440 230 490 232 520 238 V300 H0 Z" fill="#e6e6e3"/>
    </svg>
    <h1 class="brand-title">Frost &amp; Peak Coaching</h1>
    <div class="brand-mark"><span class="dot"></span><span>FPC</span></div>
  </section>

  <section class="card card-back" aria-label="Business card back">
    <svg class="card-bg" viewBox="0 0 520 300" preserveAspectRatio="none" aria-hidden="true">
      <rect x="0" y="0" width="520" height="14" fill="var(--orange)"/>
      <rect x="0" y="14" width="520" height="58" fill="var(--white)"/>
      <path d="M0 250 C80 236 160 262 240 256 C270 254 290 250 292 250 V300 H0 Z" fill="var(--white)"/>
    </svg>
    <h2 class="brand-title">Frost &amp; Peak Coaching</h2>
    <div class="holder">
      <div class="holder-name">Maya Lindqvist</div>
      <div class="holder-role">Ski Instructor &amp; Vacation Organizer</div>
    </div>
    <div class="brand-mark"><span class="dot"></span><span>FPC</span></div>

    <div class="contact-rail" aria-hidden="true">
      <svg viewBox="0 0 16 16"><rect x="4" y="1" width="8" height="14" rx="1.5" fill="none" stroke="#fff" stroke-width="1.6"/><circle cx="8" cy="12.5" r="0.9" fill="#fff"/></svg>
      <svg viewBox="0 0 16 16"><rect x="1.5" y="3.5" width="13" height="9" fill="none" stroke="#fff" stroke-width="1.5"/><path d="M1.5 3.5 L8 9 L14.5 3.5" fill="none" stroke="#fff" stroke-width="1.5"/></svg>
      <svg viewBox="0 0 16 16"><rect x="2" y="2" width="12" height="12" rx="1.5" fill="#fff"/></svg>
      <svg viewBox="0 0 16 16"><rect x="1.5" y="2.5" width="13" height="8.5" fill="none" stroke="#fff" stroke-width="1.5"/><path d="M6 14 H10 M8 11 V14" stroke="#fff" stroke-width="1.5"/></svg>
    </div>
    <ul class="contact-list">
      <li class="contact-phone">(852) 5550 1234</li>
      <li class="contact-email">maya.lind.ski@mailbox.example</li>
      <li class="contact-social">Frost &amp; Peak Coaching</li>
      <li class="contact-web">www.frostpeakcoaching.example</li>
    </ul>
  </section>

</body>
</html>
```